Camp Thornbrook 2021 Magazine Design

We are for someone to design our annual magazine/newsletter. This is a print newsletter that is a total of 20 pages. It will need to be designed in a way that is easy to share with our printers. The designer will need to be someone who is creative and easy to work with.
For those interested in this project we ask that you design 4 to 6 pages for us to view. Once we select the designer we will want the rest created in a two-week time span. For those submitting a bid please include front cover, theme & dates, mission & vision, and Make the Difference.

This link will provide the layout of the newsletter https://files.pelmarcloud.example/doc/7qzRt2LmXv9KpWnD4sHy8bCe3FaJu6NgQo5/edit?usp=sharing.

This link will provide you with the pictures that are needed and a few documents https://files.pelmarcloud.example/folders/5TbQx8WnLr2VkYcPz3HmDs7?usp=sharing

Details:
20 pages long (including covers)
8.5 x 11

Please message me if you need any further details.

Target Market(s)

Our alumni base. Covers all ages

Requirements
Must have
• Spelled out in document
Nice to have
• Spelled out in document
Should not have
• Spelled out in document

```html
<!DOCTYPE html>
<html lang="en">
<head>
<meta charset="utf-8">
<title>Camp Thornbrook 2021 Magazine – Contents &amp; Make the Difference</title>
<link rel="stylesheet" href="https://fonts.googleapis.com/css2?family=Nunito+Sans:wght@300;400;600;700&display=swap">
<style>
  :root {
    --orange: #f6a05a;
    --orange-deep: #d9844a;
    --orange-photo-light: #e8a56a;
    --orange-photo-dark: #b8733f;
    --paper-grey: #f4f5f7;
    --gutter-grey: #cfd0d2;
    --rule: rgba(255, 255, 255, 0.55);
    --white: #ffffff;
    --ink: #2b2b2b;
    --backdrop: #ffffff;
  }
  * { box-sizing: border-box; margin: 0; padding: 0; }
  html, body {
    width: 1200px; height: 840px; overflow: hidden;
    background: var(--backdrop);
    font-family: "Nunito Sans", "Avenir Next", sans-serif;
  }
  .spread {
    position: absolute; left: 20px; top: 45px;
    width: 1160px; height: 750px;
    display: flex;
  }
  .page { position: relative; width: 580px; height: 750px; overflow: hidden; }

  /* Contents page */
  .contents-page .backdrop-photo {
    position: absolute; inset: 0;
    background:
      linear-gradient(90deg, rgba(184,115,63,0.35) 0%, rgba(232,165,106,0) 40%, rgba(184,115,63,0.25) 100%),
      linear-gradient(180deg, var(--orange-photo-light) 0%, #d88d52 55%, var(--orange-photo-dark) 100%);
  }
  .contents-list {
    position: absolute; left: 64px; top: 130px; width: 450px;
    list-style: none;
  }
  .contents-item {
    display: flex; justify-content: space-between; align-items: center;
    height: 49.3px;
    border-bottom: 1px solid var(--rule);
    color: var(--white);
    font-size: 14px;
    padding-top: 4px;
  }
  .contents-item:last-child { border-bottom: none; }
  .contents-title { font-weight: 600; }
  .contents-page-ref { font-weight: 300; }

  /* Feature page */
  .feature-page { background: var(--paper-grey); }
  .feature-page .top-band {
    position: absolute; left: 0; top: 0; width: 100%; height: 375px;
    background: linear-gradient(90deg, var(--orange-deep) 0%, var(--orange) 25%, var(--orange) 100%);
  }
  .feature-page .gutter-shade {
    position: absolute; left: 0; top: 375px; width: 90px; height: 364px;
    background: linear-gradient(90deg, var(--gutter-grey) 0%, rgba(244,245,247,0) 100%);
  }
  .feature-page .bottom-band {
    position: absolute; left: 0; bottom: 0; width: 100%; height: 11px;
    background: var(--orange);
  }
  .feature-photo {
    position: absolute; left: 44px; top: 46px; width: 321px; height: 481px;
    background: linear-gradient(170deg, #6f9a4c 0%, #4f7d3a 45%, #7b8f8a 75%, #5d6f86 100%);
  }
  .body-copy {
    position: absolute;
    font-size: 8.2px; line-height: 10.3px;
    text-align: justify; color: var(--ink);
    font-weight: 400;
  }
  .body-copy p + p { margin-top: 20px; }
  .sidebar-copy { left: 388px; width: 148px; }
  .sidebar-copy.on-orange { color: var(--white); top: 141px; }
  .sidebar-copy.on-grey { top: 386px; }
  .lower-copy { left: 44px; top: 548px; width: 492px; }
</style>
</head>
<body>
<main class="spread">
  <section class="page contents-page">
    <div class="backdrop-photo" role="img" aria-label="Wooden cross-shaped post carved from a tree stump in a wooded camp, tinted orange"></div>
    <ol class="contents-list">
      <li class="contents-item"><span class="contents-title">Make the Difference</span><span class="contents-page-ref">Page 3</span></li>
      <li class="contents-item"><span class="contents-title">Golf Tournament</span><span class="contents-page-ref">Pages 4 &amp; 5</span></li>
      <li class="contents-item"><span class="contents-title">2021 Theme and Dates</span><span class="contents-page-ref">Pages 6 &amp; 7</span></li>
      <li class="contents-item"><span class="contents-title">Where Are They Now: Dana Whitfield</span><span class="contents-page-ref">Pages 8 &amp; 9</span></li>
      <li class="contents-item"><span class="contents-title">2019 Donors</span><span class="contents-page-ref">Pages 10, 11, &amp; 12</span></li>
      <li class="contents-item"><span class="contents-title">2019 Thornbrook Awards</span><span class="contents-page-ref">Page 13</span></li>
      <li class="contents-item"><span class="contents-title">Bee Rock</span><span class="contents-page-ref">Pages 14 &amp;15</span></li>
      <li class="contents-item"><span class="contents-title">Mission/Vision</span><span class="contents-page-ref">Pages 16 &amp; 17</span></li>
      <li class="contents-item"><span class="contents-title">A Place We Call Home</span><span class="contents-page-ref">Page 18</span></li>
      <li class="contents-item"><span class="contents-title">Memorials</span><span class="contents-page-ref">Page 19</span></li>
    </ol>
  </section>

  <section class="page feature-page">
    <div class="top-band"></div>
    <div class="gutter-shade"></div>
    <div class="bottom-band"></div>
    <div class="feature-photo" role="img" aria-label="Make the Difference campaign poster, July 13th – 17th: a counselor hugging two campers outdoors"></div>

    <div class="body-copy sidebar-copy on-orange">
      <p>To say that 2020 has been a challenging year is a huge understatement! March 2020 is a month none of us will soon forget. Just as we were getting ready to ramp up for the summer, things began to shut down all around us. At first we hoped it would just be a few weeks only impacting our spring retreats, but as the spring progressed, it soon became evident our 2020 summer was being threatened.</p>
      <p>In late May, we made the difficult decision to cancel all summer events. For the first time in 73 years, there would be no summer camp at Thornbrook. Our summer programming is at the heart of what we do and who we are. From the very beginning, Thornbrook’s main mission has been to share Christ through the summer camp program.</p>
    </div>

    <div class="body-copy sidebar-copy on-grey">
      <p>After dealing with the emotional aspect of not having camp this summer, we had to look at the reality of the financial impact canceling the summer would have on Thornbrook. Over 50% of our annual revenue comes from our summer programming and summer rentals. We also had to take into account the loss of our spring rentals and the possibility of fall rentals canceling. While we were confident God would provide for Thornbrook, as He always has, we weren’t sure how this would take place.</p>
    </div>

    <div class="body-copy lower-copy">
      <p>We determined that even with drastically cutting expenses, we would need an additional $50,000 to make up for the lost revenue. In late June, we received a phone call from one of our long-time Thornbrook families who was interested in helping us through this difficult time. They generously pledged $10,000 as a matching gift to help motivate the Thornbrook family to give as well. In early July, we announced the “Make the Difference” fundraising campaign. Our initial goal was to raise $10,000 in one week to receive the matching gift with the hope of substantially reducing the $50,000 deficit.</p>
      <p>The Thornbrook family showed their love and dedication through their extraordinary generosity. By the end of Monday, the first day of the campaign, we had exceeded our initial goal of $10,000 ensuring the matching gift. By the end of the week, over $64,000 was raised!</p>
      <p>While 2020 has not been the year we had hoped for, it has been a year in which Thornbrook has been blessed beyond expectations!</p>
    </div>
  </section>
</main>
</body>
</html>
```